Outdoor Real Estate Sales Banner

It should say

418 Calloway Street, East Boston
Coming Spring 2026
3 Luxury Condos
Experience refined living with elegant design and high-end finishes. Thoughtfully crafted for both comfort and sophistication.
Construction by V Construction
Now Accepting Reservations

Schedule Your Private Tour Today
Marisol Fenwick, Lanternwick Realty | 555-014-2273 | Marisol@lanternwickhomes.com
Tobias Grant, Lanternwick Realty | 555-019-8831 | Tobias@lanternwickhomes.com

Target Market(s)

30-45

Industry/Entity Type

real estate

Font styles to use
Serif

Requirements
Must have
• Colors of logo and preppy rich look
Nice to have
• herringbone incorporated the pattern
Should not have
• any loud colors

```html
<!DOCTYPE html>
<html lang="en">
<head>
<meta charset="utf-8">
<title>418 Calloway Street – Sales Banner</title>
<link rel="stylesheet" href="https://fonts.googleapis.com/css2?family=Cinzel:wght@500;600&family=Crimson+Text&family=Questrial&display=swap">
<style>
  :root{
    --backdrop:#a6a6a6;
    --navy:#223455;
    --ink:#1f2d48;
    --gold:#b39660;
    --gold-bright:#e2b563;
    --cream:#ebe2d6;
    --white:#ffffff;
  }
  html,body{margin:0;padding:0;width:1200px;height:1200px;overflow:hidden;background:var(--backdrop);}
  .banner{position:absolute;left:115px;top:225px;width:970px;height:749px;background:var(--cream);overflow:hidden;}
  .band{position:absolute;left:0;width:100%;}
  .band-top{top:0;height:141px;background:var(--navy);}
  .rule-top{top:141px;height:5px;background:var(--white);}
  .rule-bottom{top:545px;height:5px;background:var(--white);}
  .band-gold{top:550px;height:19px;background:var(--gold);}
  .band-bottom{top:569px;height:180px;background:var(--navy);}

  .building{position:absolute;left:52px;top:53px;width:347px;height:396px;
    background:linear-gradient(180deg,#e6cf95 0%,#dcc486 70%,#c9c4ba 94%,#111 97%);}

  .serif-caps{font-family:"Cinzel",serif;font-weight:500;line-height:1;position:absolute;white-space:nowrap;margin:0;}
  .address{left:437px;top:57px;color:var(--gold);font-size:29px;line-height:33px;}

  .launch-ribbon{position:absolute;left:370px;top:168px;width:548px;height:41px;
    background:linear-gradient(90deg,#d6c39f 0%,#dccbab 50%,rgba(235,226,214,0) 100%);
    border-top:1px solid #cbb58b;border-bottom:1px solid #cbb58b;}
  .launch{left:437px;top:176px;color:var(--ink);font-size:26px;font-weight:600;}
  .units{left:437px;top:229px;color:var(--gold);font-size:26px;}

  .lead{position:absolute;left:437px;top:271px;width:450px;margin:0;font-family:"Crimson Text",serif;
    font-size:18.5px;line-height:23.4px;color:var(--ink);}

  .detail{top:366px;color:var(--gold);font-size:17px;line-height:21px;}
  .detail-builder{left:437px;}
  .detail-reserve{left:660px;}
  .divider{position:absolute;left:631px;top:358px;width:1px;height:53px;background:#cdb992;}

  .cta{left:437px;top:432px;color:var(--ink);font-size:20.5px;font-weight:600;}

  .portrait{position:absolute;width:149px;height:149px;border-radius:50%;
    background:radial-gradient(circle at 50% 42%,#c7a97a 0%,#b39660 55%,#2d3a55 100%);}
  .portrait-left{left:86px;top:485px;}
  .portrait-right{left:736px;top:485px;}

  .brand-disc{position:absolute;left:398px;top:484px;width:170px;height:170px;border-radius:50%;background:var(--navy);}
  .brand{position:absolute;left:0;width:966px;top:638px;text-align:center;font-family:"Cinzel",serif;font-weight:600;color:var(--gold-bright);}
  .brand-name{display:block;font-size:38px;line-height:40px;}
  .brand-sub{display:block;font-size:17px;line-height:22px;letter-spacing:17px;padding-left:17px;}

  .agent{position:absolute;top:647px;width:330px;text-align:center;color:var(--gold);}
  .agent-left{left:-5px;}
  .agent-right{left:645px;}
  .agent-name{font-family:"Questrial",sans-serif;font-size:23px;line-height:26px;margin:0 0 2px;}
  .agent-line{font-family:"Crimson Text",serif;font-size:14.5px;line-height:19px;margin:0;}
</style>
</head>
<body>
<div class="banner">
  <div class="band band-top"></div>
  <div class="band rule-top"></div>
  <div class="band rule-bottom"></div>
  <div class="band band-gold"></div>
  <div class="band band-bottom"></div>

  <div class="building" role="img" aria-label="Front elevation rendering of a three-storey yellow clapboard townhouse with white trim and entry stair"></div>

  <h1 class="serif-caps address">418 Calloway Street<br>East Boston</h1>

  <div class="launch-ribbon"></div>
  <p class="serif-caps launch">Coming Spring 2026</p>
  <p class="serif-caps units">3 Luxury Condos</p>

  <p class="lead">Experience refined living with elegant design and high-end finishes. Thoughtfully crafted for both comfort and sophistication.</p>

  <p class="serif-caps detail detail-builder">Construction by<br>V Construction</p>
  <div class="divider"></div>
  <p class="serif-caps detail detail-reserve">Now Accepting<br>Reservations</p>

  <p class="serif-caps cta">Schedule Your Private Tour Today</p>

  <div class="portrait portrait-left" role="img" aria-label="Portrait photo of agent Tobias Grant"></div>
  <div class="portrait portrait-right" role="img" aria-label="Portrait photo of agent Marisol Fenwick"></div>

  <div class="brand-disc"></div>
  <div class="brand">
    <span class="brand-name">LANTERNWICK</span>
    <span class="brand-sub">REALTY</span>
  </div>

  <div class="agent agent-left">
    <p class="agent-name">Tobias Grant</p>
    <p class="agent-line">Lanternwick Realty &nbsp;|&nbsp; 555-019-8831</p>
    <p class="agent-line">Tobias@lanternwickhomes.com</p>
  </div>
  <div class="agent agent-right">
    <p class="agent-name">Marisol Fenwick</p>
    <p class="agent-line">Lanternwick Realty &nbsp;|&nbsp; 555-014-2273</p>
    <p class="agent-line">Marisol@lanternwickhomes.com</p>
  </div>
</div>
</body>
</html>
```